Create our new Brightcup Coffee Syrup Label designs. A delicious job!

Design a front label for a range of coffee syrup flavours. The brand is 'Brightcup Coffee Syrups'. The flavours, vanilla, hazelnut and caramel.
Our coffee syrups are made with only natural colours and flavours and are positioned in the popular premium space in Australian and international cafes.
The labels will be applied to 750 ml Boston Bottles (see attached image).
Given that coffee syrups are often positioned in high visibility locations in cafes, they can be considered as objects of functional beauty.
This range is a sub brand for our company and I have attached our main brand images in the flavours we want. we want this brand to look different to this Marlowe branded range, but included the image to show what we are currently doing in this space.
The different flavours can be identified by a combination of colour and text, which may be a line or section of the otherwise same overall design.
We are going to do a 2 part label with the front just carrying Brand and flavour descriptors plus 750 ml.
Total Bottle height is 240 mm bottle width is 70 mm

Target Market(s)

Cafe patrons, primarily women, 18-35, Middle class in terms of economics, regular cafe patrons. Who are looking for a guilt free treat in their busy day.

Logo Text

Brightcup Coffee Syrups Vanilla (or Hazelnut, or Caramel) 750 ml

Logo styles of interest
Pictorial/Combination Logo
Font styles to use
Sans Serif

Colors

Designer to choose colors to be used in the design.

Requirements
Must have
• A clear design, which is a combination of font and image. it needs to be legible from up to 2m away (across a counter in a cafe).
• We would like to see a device, which may be a gold drop, that may be the 'brightcup' meant to the coffee.
• The way our coffee syrups are used is by adding a small amount (15 ml) to a cup
• of coffee, this adds both flavour and sweetness to the overall coffee experience, and cafes charge a premium for this service. We want our package to show this will be a great thing to do.
• We have a few options in terms of Label stock. We can print on a foil, that will allow a metallic sheen to come through the colours (see example of the Marlowe branded bottles.
Nice to have
• We are looking for a modern, clean and distinctive look and feel to this range.
• I have added a key line for the front and back label, however we can create a different label die line should the design warrant that. Note this is just for the front label.
Should not have
• Difficult to read fonts or imagery that is not clear.
• Should look different to the Marlowe branded product range.

```html
<!DOCTYPE html>
<html lang="en">
<head>
<meta charset="utf-8">
<title>Brightcup Coffee Syrups – Front Labels</title>
<link rel="stylesheet" href="https://fonts.googleapis.com/css2?family=Big+Shoulders+Display:wght@500;600&family=Josefin+Slab:wght@700&display=swap">
<style>
  :root {
    --ink: #000000;
    --paper: #ffffff;
    --hazelnut: #e3a98c;
    --caramel: #f04e23;
    --vanilla: #f8a51c;
  }
  html, body {
    margin: 0;
    padding: 0;
    overflow: hidden;
  }
  .canvas {
    width: 1200px;
    height: 1200px;
    background: var(--ink);
    display: flex;
    align-items: center;
    justify-content: center;
    gap: 50px;
    overflow: hidden;
  }
  .label {
    width: 336px;
    height: 411px;
    display: block;
  }
  .label--hazelnut { --flavour: var(--hazelnut); }
  .label--caramel  { --flavour: var(--caramel); }
  .label--vanilla  { --flavour: var(--vanilla); }

  .label__frame {
    fill: none;
    stroke: var(--flavour);
    stroke-width: 9;
    stroke-linecap: round;
    stroke-linejoin: round;
  }
  .label__brand {
    font-family: "Big Shoulders Display", "Arial Narrow", sans-serif;
    font-weight: 500;
    font-size: 64px;
    fill: var(--paper);
  }
  .label__badge { fill: var(--flavour); }
  .label__flavour {
    font-family: "Big Shoulders Display", "Arial Narrow", sans-serif;
    font-weight: 600;
    font-size: 40px;
    fill: var(--ink);
  }
  .label__descriptor {
    font-family: "Josefin Slab", Georgia, serif;
    font-weight: 700;
    font-size: 19px;
    letter-spacing: 6px;
    fill: var(--paper);
  }
  .label__volume {
    font-family: "Josefin Slab", Georgia, serif;
    font-weight: 700;
    font-size: 16px;
    letter-spacing: 3px;
    fill: var(--paper);
  }
  .label__dot { fill: var(--flavour); }
</style>
</head>
<body>
<main class="canvas">

  <svg class="label label--hazelnut" viewBox="0 0 270 330" aria-labelledby="hazelnut-title">
    <title id="hazelnut-title">Brightcup Hazelnut Coffee Syrup, 750 ml</title>
    <path class="label__frame" d="M24 42 H12 Q6 42 6 48 V316 Q6 322 12 322 H258 Q264 322 264 316 V48 Q264 42 258 42 H246"/>
    <text class="label__brand" x="135" y="62" text-anchor="middle" textLength="206" lengthAdjust="spacingAndGlyphs">BRIGHTCUP</text>
    <circle class="label__badge" cx="135" cy="172" r="70"/>
    <text class="label__flavour" x="135" y="186" text-anchor="middle" textLength="104" lengthAdjust="spacingAndGlyphs">HAZELNUT</text>
    <path id="arc-hazelnut" d="M37 180 A98 98 0 0 0 233 180" fill="none"/>
    <text class="label__descriptor"><textPath href="#arc-hazelnut" startOffset="50%" text-anchor="middle">COFFEE <tspan class="label__dot">•</tspan> SYRUP</textPath></text>
    <circle class="label__dot" cx="38" cy="176" r="3.5"/>
    <circle class="label__dot" cx="232" cy="176" r="3.5"/>
    <text class="label__volume" x="135" y="308" text-anchor="middle">750 ML</text>
  </svg>

  <svg class="label label--caramel" viewBox="0 0 270 330" aria-labelledby="caramel-title">
    <title id="caramel-title">Brightcup Caramel Coffee Syrup, 750 ml</title>
    <path class="label__frame" d="M24 42 H12 Q6 42 6 48 V316 Q6 322 12 322 H258 Q264 322 264 316 V48 Q264 42 258 42 H246"/>
    <text class="label__brand" x="135" y="62" text-anchor="middle" textLength="206" lengthAdjust="spacingAndGlyphs">BRIGHTCUP</text>
    <circle class="label__badge" cx="135" cy="172" r="70"/>
    <text class="label__flavour" x="135" y="186" text-anchor="middle" textLength="98" lengthAdjust="spacingAndGlyphs">CARAMEL</text>
    <path id="arc-caramel" d="M37 180 A98 98 0 0 0 233 180" fill="none"/>
    <text class="label__descriptor"><textPath href="#arc-caramel" startOffset="50%" text-anchor="middle">COFFEE <tspan class="label__dot">•</tspan> SYRUP</textPath></text>
    <circle class="label__dot" cx="38" cy="176" r="3.5"/>
    <circle class="label__dot" cx="232" cy="176" r="3.5"/>
    <text class="label__volume" x="135" y="308" text-anchor="middle">750 ML</text>
  </svg>

  <svg class="label label--vanilla" viewBox="0 0 270 330" aria-labelledby="vanilla-title">
    <title id="vanilla-title">Brightcup Vanilla Coffee Syrup, 750 ml</title>
    <path class="label__frame" d="M24 42 H12 Q6 42 6 48 V316 Q6 322 12 322 H258 Q264 322 264 316 V48 Q264 42 258 42 H246"/>
    <text class="label__brand" x="135" y="62" text-anchor="middle" textLength="206" lengthAdjust="spacingAndGlyphs">BRIGHTCUP</text>
    <circle class="label__badge" cx="135" cy="172" r="70"/>
    <text class="label__flavour" x="135" y="186" text-anchor="middle" textLength="92" lengthAdjust="spacingAndGlyphs">VANILLA</text>
    <path id="arc-vanilla" d="M37 180 A98 98 0 0 0 233 180" fill="none"/>
    <text class="label__descriptor"><textPath href="#arc-vanilla" startOffset="50%" text-anchor="middle">COFFEE <tspan class="label__dot">•</tspan> SYRUP</textPath></text>
    <circle class="label__dot" cx="38" cy="176" r="3.5"/>
    <circle class="label__dot" cx="232" cy="176" r="3.5"/>
    <text class="label__volume" x="135" y="308" text-anchor="middle">750 ML</text>
  </svg>

</main>
</body>
</html>
```